Business Card Design Project

Hi. We need a new business card for Brightfield Partners, a consultancy that helps people with online marketing strategy and solutions.

We have a new logo and now need the info presented - front and back of business card.

FRONT

Logo

Online strategy, consulting and coaching
Varlo Admarket consulting
Search Engine Optimisation
Internet Lead Generation
Domain name broking

BACK

Tom Bradwell-Jones
+ 61 83215 9076
+ 61 (0) 418 536 207
tom@brightfieldpartners.com.au
www.brightfieldpartners.com.au

Talkora: tombradwelljones
PO Box 312, Corrin Bay, Western Australia 6184

Target Market(s)

Business owners, corporates

Industry/Entity Type

Marketing

Requirements
Must have
• double sided
size: 86 x 54mm
supplied as one pdf with crop marks shown (+- 1mm, with 2-3 mm bleed)

```html
<!DOCTYPE html>
<html lang="en">
<head>
<meta charset="utf-8">
<title>Brightfield Partners – Business Card</title>
<link rel="stylesheet" href="https://fonts.googleapis.com/css2?family=Arimo:wght@400;700&display=swap">
<style>
  :root {
    --page-bg: #ececec;
    --card-white: #ffffff;
    --brand-blue: #1f4d89;
    --brand-navy: #1a3f75;
    --brand-orange: #f28c28;
    --link-blue: #2f63b0;
    --ink: #111111;
    --on-blue: #ffffff;
  }
  * { box-sizing: border-box; margin: 0; padding: 0; }
  html, body { width: 1200px; height: 1000px; overflow: hidden; }
  body {
    background: var(--page-bg);
    font-family: "Arimo", Arial, sans-serif;
    position: relative;
  }
  .card {
    position: absolute;
    top: 351px;
    width: 538px;
    height: 298px;
    border-radius: 18px;
    overflow: hidden;
    background: var(--card-white);
    box-shadow: 0 6px 14px rgba(0,0,0,0.25);
  }
  .card--front { left: 46px; }
  .card--back { left: 618px; }
  .card__top { height: 148px; position: relative; }
  .card__band {
    height: 150px;
    background: var(--brand-blue);
    color: var(--on-blue);
    position: relative;
  }
  /* front */
  .brand {
    position: absolute;
    top: 40px; left: 0; right: 0;
    display: flex; align-items: center; justify-content: center; gap: 12px;
  }
  .brand__dot {
    width: 30px; height: 30px; border-radius: 50%;
    background: var(--brand-orange);
  }
  .brand__name {
    font-size: 34px; font-weight: 700; color: var(--brand-navy);
    letter-spacing: -0.5px;
  }
  .brand__url {
    position: absolute; top: 110px; left: 0; right: 0;
    text-align: center; font-size: 12px; font-weight: 700;
    letter-spacing: 2.4px; color: var(--link-blue);
  }
  .services {
    list-style: none; text-align: center;
    padding-top: 26px;
    font-size: 13.5px; font-weight: 700; line-height: 20px;
  }
  /* back */
  .person {
    position: absolute; top: 66px; left: 0; right: 0;
    text-align: center; font-size: 26px; font-weight: 700; color: var(--ink);
  }
  .contact {
    position: absolute; font-size: 13.5px; font-weight: 700;
  }
  .contact--left { left: 24px; top: 54px; line-height: 26px; }
  .contact--right { right: 28px; top: 55px; text-align: right; line-height: 17px; }
</style>
</head>
<body>
  <section class="card card--front" aria-label="Card front">
    <div class="card__top">
      <div class="brand">
        <span class="brand__dot"></span>
        <span class="brand__name">Brightfield Partners</span>
      </div>
      <div class="brand__url">brightfieldpartners.com.au</div>
    </div>
    <div class="card__band">
      <ul class="services">
        <li>Online strategy, consulting and coaching</li>
        <li>Search Engine Optimisation</li>
        <li>Varlo Admarket consulting</li>
        <li>Internet Lead Generation</li>
        <li>Domain name broking</li>
      </ul>
    </div>
  </section>

  <section class="card card--back" aria-label="Card back">
    <div class="card__top">
      <div class="person">Tom Bradwell-Jones</div>
    </div>
    <div class="card__band">
      <div class="contact contact--left">
        <div>Talkora: tombradwelljones</div>
        <div>tom@brightfieldpartners.com.au</div>
        <div>www.brightfieldpartners.com.au</div>
      </div>
      <div class="contact contact--right">
        <div>+ 61 83215 9076</div>
        <div>+ 61 (0) 418 536 207</div>
        <div>PO Box 312, Corrin Bay</div>
        <div>Western Australia 6184</div>
      </div>
    </div>
  </section>
</body>
</html>
```